Start-up company developing economical and ecological hydrogen peroxide generator needs an attractiv

We need a powerpoint design for a start-up company based in Montreal called Vorbelle currently seeking to raise funds from investors. We develop an electrochemical hydrogen peroxide generator based on new generation catalysts.

These generators allow industrial users of hydrogen peroxide to generate it onsite economically and ecologically, as opposed to buying it from the major suppliers who make it large production plants using more polluting methods and need to transport it to customers over long distances.

We would like to see designs that have a cleantech technology and green chemistry feel. Colors that evoke a sense of environmental sustainability are desired.

The final design should communicate technological innovation that makes the world a cleaner and healthier place to live.

Target Market(s)

Industrial users or producers of of hydrogen peroxide

Industry/Entity Type

It Company

Font styles to use
Sans Serif

Colors
0255a3
3276b5
85acd3
9bcb3b
add136
e3eebf

Requirements
Must have
• Clean, attractive, professional and advanced technology look.
• Our slogan is: Catalyst for innovation
Nice to have
• The cover page should have our logo and our slogan. It should also have some graphics that pertain to technology and green chemistry. The perception that one should have when looking at it is that the company is developing a clean chemical manufacturing technology that is more environmentally friendly.
• Each other template page should have our logo discretely included in it.
• Other than the cover page, the template pages should not be too crowded with design elements. There should be lots of clear space to add material.
• I have uploaded some inspirational images that can be used to help come up with some designs.

```html
<!DOCTYPE html>
<html lang="en">
<head>
<meta charset="utf-8">
<title>Vorbelle – Slide Templates</title>
<link rel="stylesheet" href="https://fonts.googleapis.com/css2?family=Open+Sans:wght@400;600;700&display=swap">
<style>
  :root {
    --brand-blue: #0255a3;
    --mid-blue: #3276b5;
    --light-blue: #85acd3;
    --canvas-grey: #d6d7d9;
    --slide-white: #ffffff;
    --row-grey: #e4e5e7;
    --text-dark: #2b2b2b;
    --text-muted: #6b6b6b;
    --swoosh-grey: #b9bbbe;
  }
  * { box-sizing: border-box; margin: 0; padding: 0; }
  html, body { width: 849px; height: 1200px; overflow: hidden; }
  body {
    background: var(--canvas-grey);
    font-family: "Open Sans", Arial, sans-serif;
    color: var(--text-dark);
    position: relative;
  }
  .slide {
    position: absolute;
    left: 14px;
    width: 821px;
    height: 552px;
    background: var(--slide-white);
    overflow: hidden;
    box-shadow: 0 1px 3px rgba(0,0,0,.15);
  }
  .slide--tables { top: 14px; }
  .slide--team { top: 630px; }

  .slide-header { position: absolute; left: 0; top: 18px; width: 100%; height: 80px; }
  .header-bar {
    position: absolute; left: 18px; top: 6px;
    width: 4px; height: 50px; background: var(--brand-blue);
  }
  .slide-title {
    position: absolute; left: 32px; top: 0;
    font-size: 29px; font-weight: 400; color: var(--brand-blue);
    line-height: 38px;
  }
  .slide-slogan {
    position: absolute; left: 33px; top: 40px;
    font-size: 13px; color: var(--text-muted);
  }
  .brand-name {
    position: absolute; right: 30px; top: 6px;
    font-size: 24px; font-weight: 600; color: var(--brand-blue);
  }

  .data-table {
    position: absolute; left: 108px; top: 130px;
    width: 600px; border-collapse: collapse;
    font-size: 14px;
  }
  .data-table th {
    background: var(--brand-blue); color: #fff;
    font-weight: 600; text-align: left;
    padding: 6px 12px; height: 50px; line-height: 18px;
  }
  .data-table td { padding: 0 12px; height: 40px; }
  .data-table tbody tr:nth-child(even) td { background: var(--row-grey); }

  .slide-footer { position: absolute; left: 0; bottom: 0; width: 100%; height: 80px; }
  .slide-number {
    position: absolute; right: 18px; bottom: 24px;
    width: 96px; height: 30px; background: var(--brand-blue);
    color: #fff; font-size: 14px; text-align: right;
    padding-right: 10px; line-height: 30px;
  }

  .team-grid {
    position: absolute; left: 30px; top: 118px;
    display: flex;
  }
  .member { width: 185px; text-align: center; }
  .member-photo {
    width: 80px; height: 80px; margin: 0 auto;
    border-radius: 50%; border: 3px solid var(--light-blue);
    background: linear-gradient(160deg, #c9d3dd, #7f8b97);
  }
  .member-name {
    margin-top: 16px; font-size: 15px; font-weight: 400; color: var(--mid-blue);
  }
  .member-role { margin-top: 2px; font-size: 12px; color: var(--text-dark); }
  .member-bio {
    margin: 14px auto 0; width: 136px;
    font-size: 12px; line-height: 18px; color: var(--text-dark);
  }
</style>
</head>
<body>

<section class="slide slide--tables">
  <header class="slide-header">
    <span class="header-bar"></span>
    <h1 class="slide-title">Our Tables</h1>
    <p class="slide-slogan">Catalyst for innovation</p>
    <span class="brand-name">Vorbelle</span>
  </header>

  <table class="data-table">
    <thead>
      <tr><th>Company<br>Name</th><th>2000-01</th><th>2001-02</th><th>2003-04</th><th>2004-05</th></tr>
    </thead>
    <tbody>
      <tr><td>ABCE</td><td>68</td><td>2</td><td>61</td><td>20</td></tr>
      <tr><td>EDGA</td><td>1</td><td>23</td><td>3263</td><td>653</td></tr>
      <tr><td>ALKJDF</td><td>3323</td><td>0323</td><td>2413</td><td>3230</td></tr>
      <tr><td>ASDF</td><td>32353</td><td>035603</td><td>23253</td><td>230.</td></tr>
      <tr><td>DFGH</td><td>35665</td><td>32356</td><td>323562</td><td>3226</td></tr>
      <tr><td>TYTRY</td><td>3265</td><td>3265</td><td>326</td><td>63</td></tr>
      <tr><td>AE9RAGML</td><td>21545</td><td>4852163</td><td>6632323</td><td>646323</td></tr>
    </tbody>
  </table>

  <footer class="slide-footer">
    <svg width="821" height="80" viewBox="0 0 821 80" aria-hidden="true">
      <path d="M0 62 C200 40 420 78 821 50 L821 80 L0 80 Z" fill="var(--row-grey)"/>
      <path d="M0 70 C240 50 470 84 821 60" fill="none" stroke="var(--swoosh-grey)" stroke-width="2"/>
    </svg>
    <div class="slide-number">06</div>
  </footer>
</section>

<section class="slide slide--team">
  <header class="slide-header">
    <span class="header-bar"></span>
    <h1 class="slide-title">Our Team members</h1>
    <p class="slide-slogan">Catalyst for innovation</p>
    <span class="brand-name">Vorbelle</span>
  </header>

  <div class="team-grid">
    <article class="member">
      <div class="member-photo" role="img" aria-label="Portrait photo of team member"></div>
      <h2 class="member-name">Daniel Morel Hart</h2>
      <p class="member-role">His designation</p>
      <p class="member-bio">We need a powerpoint design for a start-up company based in Montreal called Vorbelle currently seeking to</p>
    </article>
    <article class="member">
      <div class="member-photo" role="img" aria-label="Portrait photo of team member"></div>
      <h2 class="member-name">Daniel Morel Hart</h2>
      <p class="member-role">His designation</p>
      <p class="member-bio">We need a powerpoint design for a start-up company based in Montreal called Vorbelle currently seeking to</p>
    </article>
    <article class="member">
      <div class="member-photo" role="img" aria-label="Portrait photo of team member"></div>
      <h2 class="member-name">Daniel Morel Hart</h2>
      <p class="member-role">His designation</p>
      <p class="member-bio">We need a powerpoint design for a start-up company based in Montreal called Vorbelle currently seeking to</p>
    </article>
    <article class="member">
      <div class="member-photo" role="img" aria-label="Portrait photo of team member"></div>
      <h2 class="member-name">Daniel Morel Hart</h2>
      <p class="member-role">His designation</p>
      <p class="member-bio">We need a powerpoint design for a start-up company based in Montreal called Vorbelle currently seeking to</p>
    </article>
  </div>

  <footer class="slide-footer">
    <svg width="821" height="80" viewBox="0 0 821 80" aria-hidden="true">
      <path d="M0 62 C200 40 420 78 821 50 L821 80 L0 80 Z" fill="var(--row-grey)"/>
      <path d="M0 70 C240 50 470 84 821 60" fill="none" stroke="var(--swoosh-grey)" stroke-width="2"/>
    </svg>
    <div class="slide-number">07</div>
  </footer>
</section>

</body>
</html>
```